Webbanner-Design für Verkäufer von versilberten Wohnaccessoires
Zielgruppe
Wir verkaufen versilberte Wohnaccessoires (Luxus)
www.morvani-casa.de
Aufgabenstellung
Wir sind auf der Suche nach drie Bannern die bei uns auf der Webseite durchlaufen (www.morvani-casa.de)
1. Banner:
Schriftzug: Deko-Highlights für das perfekte Dinner
3x Buttons: GLÄSER / LEUCHTER / KARAFFEN
2. Banner: Die Teelichterkerze - Entdecke die genial Idee
2x Buttons: Kerze mit Ø 8cm / Kerze mit Ø 10cm
3. Banner: Die gemütlichste Dekoration zu Weihnachten
3x Buttons: Teelichter / Adventskränze / Dekoration
4. Banner: Glänzende Bilderrahmen - das perfekte Geschenk!
3x Buttons: 10x15cm / 13x18cm / 15x20cm

```html
<!DOCTYPE html>
<html lang="de">
<head>
<meta charset="utf-8">
<title>Morvani – Die Teelichterkerze</title>
<link href="https://fonts.googleapis.com/css2?family=Montserrat:wght@300;400;500&family=Open+Sans:wght@400;600;700&family=Cormorant+Garamond:wght@500&display=swap" rel="stylesheet">
<style>
  :root{
    --ink:#1a1a1a;
    --text:#333;
    --white:#fff;
    --bar:#161616;
    --pill:#ececec;
    --btn-light:#ededeb;
    --btn-dark:#111;
  }
  *{box-sizing:border-box;margin:0;padding:0}
  html,body{width:1200px;height:607px;overflow:hidden;background:var(--white);font-family:"Open Sans",sans-serif;color:var(--text)}
  .page{position:relative;width:1200px;height:607px;overflow:hidden}
  .cookie-note{position:absolute;left:161px;top:16px;font-size:9.5px;color:var(--ink)}
  .cookie-accept{position:absolute;left:956px;top:8px;width:88px;height:31px;background:var(--btn-dark);color:var(--white);font-size:9.5px;font-weight:700;display:flex;align-items:center;justify-content:center}
  .brand{position:absolute;left:161px;top:58px;width:110px;height:45px;display:flex;align-items:center;gap:6px;font-family:"Cormorant Garamond",serif;font-size:25px;font-weight:500;color:var(--ink);letter-spacing:1px}
  .brand-dot{width:9px;height:9px;border-radius:50%;background:var(--ink)}
  .utility{position:absolute;top:46px;height:28px;display:flex;align-items:center;font-size:9.5px;color:var(--ink)}
  .utility svg{margin-right:3px}
  .u-search{left:699px}
  .u-service{left:766px}
  .u-account{left:857px}
  .u-cart{left:943px;width:93px;background:var(--pill);justify-content:center;font-weight:600}
  .main-nav{position:absolute;top:88px;left:426px;display:flex;gap:12px;font-size:11px;color:var(--ink);align-items:center;white-space:nowrap}
  .usp-bar{position:absolute;left:0;top:118px;width:1200px;height:27px;background:var(--bar);color:var(--white);font-size:9.5px}
  .usp{position:absolute;top:0;height:27px;display:flex;align-items:center;gap:6px}
  .hero{position:absolute;left:161px;top:145px;width:876px;height:322px;overflow:hidden}
  .hero-photo{position:absolute;top:0;height:322px}
  .hero-photo.left{left:0;width:437px;background:radial-gradient(ellipse at 45% 45%,#e3ddd3 0%,#bfa48a 40%,#7a4a2a 80%,#5a341c 100%)}
  .hero-photo.right{left:437px;width:439px;background:radial-gradient(circle at 60% 40%,#ece7de 0%,#d8c8b6 28%,#a0673e 55%,#6b3d20 100%)}
  .hero-title{position:absolute;left:0;width:876px;top:128px;text-align:center;font-family:"Montserrat",sans-serif;font-weight:300;font-size:42px;color:var(--white);letter-spacing:-1.5px}
  .hero-sub{position:absolute;left:0;width:876px;top:180px;text-align:center;font-family:"Montserrat",sans-serif;font-weight:300;font-size:27px;color:var(--white);letter-spacing:-1px}
  .cta{position:absolute;top:237px;height:41px;display:flex}
  .cta-label{width:162px;background:var(--btn-light);display:flex;align-items:center;justify-content:center;font-family:"Montserrat",sans-serif;font-weight:500;font-size:14px;color:var(--ink);letter-spacing:-.5px}
  .cta-arrow{width:42px;background:var(--btn-dark);display:flex;align-items:center;justify-content:center}
  .cta.small{left:221px}
  .cta.large{left:451px}
  .tile{position:absolute;top:481px;width:207px;height:140px;border:1px solid #e4e4e4}
  .t1{left:161px;background:linear-gradient(160deg,#bdb8ae,#9c968a 60%,#c9bc8f)}
  .t2{left:384px;background:linear-gradient(160deg,#e9e9e7,#b9a58a 55%,#d9c9a8)}
  .t3{left:606px;background:linear-gradient(160deg,#e2d9c8,#c8bba1 50%,#8a9a5a)}
  .t4{left:829px;background:linear-gradient(160deg,#e9eaec,#d8d8da 60%,#f3f3f3)}
</style>
</head>
<body>
<div class="page">
  <p class="cookie-note">Diese Website verwendet Cookies, um Ihnen die bestmögliche Funktionalität bieten zu können.</p>
  <div class="cookie-accept">Einverstanden</div>

  <div class="brand"><span class="brand-dot"></span>MORVANI</div>

  <div class="utility u-search"><svg width="9" height="9" viewBox="0 0 10 10"><circle cx="4" cy="4" r="3" fill="none" stroke="#1a1a1a" stroke-width="1.4"/><line x1="6.2" y1="6.2" x2="9.3" y2="9.3" stroke="#1a1a1a" stroke-width="1.5"/></svg>Suchen</div>
  <div class="utility u-service">Service/Hilfe&nbsp;<svg width="8" height="5" viewBox="0 0 8 5"><path d="M1 1l3 3 3-3" fill="none" stroke="#1a1a1a" stroke-width="1.2"/></svg></div>
  <div class="utility u-account">Mein Konto&nbsp;<svg width="8" height="5" viewBox="0 0 8 5"><path d="M1 1l3 3 3-3" fill="none" stroke="#1a1a1a" stroke-width="1.2"/></svg></div>
  <div class="utility u-cart"><svg width="11" height="9" viewBox="0 0 11 9"><path d="M0 1h2l1.5 5h6l1-4H3" fill="#1a1a1a" stroke="#1a1a1a"/><circle cx="4" cy="8" r="1" fill="#1a1a1a"/><circle cx="9" cy="8" r="1" fill="#1a1a1a"/></svg>Warenkorb</div>

  <nav class="main-nav">
    <svg width="11" height="10" viewBox="0 0 11 10"><path d="M5.5 0L0 5h1.5v5h3V7h2v3h3V5H11z" fill="#1a1a1a"/></svg>
    <span>Geschenke</span><span>NEU</span><span>Material</span><span>Bar</span><span>Tafel</span><span>Wohnen</span><span>Accessoires</span><span>Kinder</span><span>Lumera Porzellan</span><span>Weihnachten</span><span>SALE</span>
  </nav>

  <div class="usp-bar">
    <div class="usp" style="left:161px"><svg width="10" height="7" viewBox="0 0 10 7"><rect x="0" y="0" width="6" height="5" fill="#fff"/><path d="M6 2h2.5L10 4v1H6z" fill="#fff"/><circle cx="2" cy="6" r="1" fill="#fff"/><circle cx="8" cy="6" r="1" fill="#fff"/></svg>Kostenloser Versand ab € 20,- Bestellwert</div>
    <div class="usp" style="left:455px"><svg width="10" height="10" viewBox="0 0 10 10"><circle cx="5" cy="5" r="4" fill="none" stroke="#fff" stroke-width="1.1"/><path d="M5 2.5V5h2" fill="none" stroke="#fff" stroke-width="1.1"/></svg>Versand innerhalb von 48h*</div>
    <div class="usp" style="left:663px"><svg width="9" height="9" viewBox="0 0 9 9"><path d="M0 4h2v5H0zM3 4l2-4c1 0 1.2 1 1 2.5H9l-1 6.5H3z" fill="#fff"/></svg>30 Tage Geld-Zurück-Garantie</div>
    <div class="usp" style="left:894px"><svg width="9" height="9" viewBox="0 0 9 9"><path d="M1 1l2-1 1.5 2.5L3 3.5c.7 1.3 1.3 1.9 2.5 2.5l1-1.5L9 6 8 8C4 8 1 5 1 1z" fill="#fff"/></svg>24h Hotline 0400 - 12 34 567</div>
  </div>

  <section class="hero">
    <div class="hero-photo left" role="img" aria-label="Hand setzt ein Teelicht in eine weiße Stumpenkerze auf einem Holztisch"></div>
    <div class="hero-photo right" role="img" aria-label="Hand hält die Unterseite einer weißen Teelichterkerze"></div>
    <h1 class="hero-title">Die Teelichterkerze</h1>
    <p class="hero-sub">Entdecke die genial Idee</p>
    <a class="cta small"><span class="cta-label">KERZE MIT Ø 8CM</span><span class="cta-arrow"><svg width="22" height="8" viewBox="0 0 22 8"><path d="M0 4h21M17 1l4 3-4 3" fill="none" stroke="#fff" stroke-width="1"/></svg></span></a>
    <a class="cta large"><span class="cta-label">KERZE MIT Ø 10CM</span><span class="cta-arrow"><svg width="22" height="8" viewBox="0 0 22 8"><path d="M0 4h21M17 1l4 3-4 3" fill="none" stroke="#fff" stroke-width="1"/></svg></span></a>
  </section>

  <div class="tile t1" role="img" aria-label="Versilberter Becher mit Gin- und Tonic-Flaschen"></div>
  <div class="tile t2" role="img" aria-label="Gedeckter Frühstückstisch mit Eierbecher und silbernem Hirsch"></div>
  <div class="tile t3" role="img" aria-label="Silberne Bilderrahmen mit Blumen auf einem Sofa"></div>
  <div class="tile t4" role="img" aria-label="Helles Wohnzimmer mit Bilderwand und Kerzen"></div>
</div>
</body>
</html>
```